8 x 8 Social Media Design - Boss Program #1

Why be a regular Agent, when you can be a Boss?
HALO PRIMEVIEW HOMES GROUP
We offer Four Levels of Participation
You Increase your Earning Potential at Each Level
Level One - Learn to Earn Additional Income Through....
Mortgage Originations - Dual Licensing / No Additional Work
Real Estate Investing - Invest Jointly with Us
Agent Recruitment - Up to 10% Override
Level Two - Team Leader
Level Three - Minority Halo Franchise Ownership
Level Four - Majority Halo Franchise Ownership
For more information visit us at www.jobsathalopview.com and request a meeting with our Managing Broker, Mr. Gordon Malvery.

```html
<!DOCTYPE html>
<html lang="en">
<head>
<meta charset="utf-8">
<title>Boss Program – Halo Primeview Homes Group</title>
<link rel="stylesheet" href="https://fonts.googleapis.com/css2?family=Montserrat:wght@400;500;600;700;800&family=Bebas+Neue&display=swap">
<style>
  :root {
    --teal: #1b8f98;
    --teal-light: #4fb3b9;
    --teal-dark: #12666d;
    --ink: #000000;
    --paper: #ffffff;
    --text: #1a1a1a;
  }
  * { box-sizing: border-box; margin: 0; padding: 0; }
  html, body { width: 1200px; height: 1200px; overflow: hidden; background: var(--paper); }
  .poster {
    position: relative;
    width: 1200px;
    height: 1200px;
    background: var(--paper);
    font-family: "Montserrat", Arial, sans-serif;
    color: var(--ink);
    overflow: hidden;
  }
  .backdrop { position: absolute; inset: 0; }
  .headline { position: absolute; left: 41px; top: 40px; line-height: 1; }
  .headline .lead { font-weight: 800; font-size: 40px; letter-spacing: 0.2px; }
  .headline .lead-2 { font-weight: 500; font-size: 70px; margin-top: 6px; letter-spacing: 0.5px; }
  .headline .big {
    font-weight: 800;
    font-size: 182px;
    line-height: 0.82;
    letter-spacing: -2px;
  }
  .headline .be-a { margin-top: 34px; }
  .headline .boss { color: var(--teal); margin-top: 20px; }
  .offer {
    position: absolute; left: 41px; top: 548px;
    font-family: "Bebas Neue", "Oswald", sans-serif;
    font-size: 51px; line-height: 46px;
    color: var(--ink);
  }
  .levels {
    position: absolute; left: 41px; top: 702px;
    list-style: none;
    font-size: 19.5px; line-height: 24.2px;
    color: var(--text);
  }
  .levels li { position: relative; padding-left: 20px; }
  .levels li.detail { list-style: none; }
  .levels li .tick { position: absolute; left: 0; top: 6px; width: 14px; height: 14px; }
  .levels strong { font-weight: 600; color: var(--ink); }
  .footer-info { position: absolute; left: 60px; top: 1016px; color: var(--paper); }
  .footer-info h2 { font-weight: 600; font-size: 42px; letter-spacing: 0.5px; line-height: 1; }
  .footer-info .rule { height: 2px; background: var(--paper); margin: 8px 0 6px; width: 560px; }
  .footer-info .rule.short { width: 394px; margin: 6px 0 8px; }
  .footer-info p { font-size: 25px; line-height: 31px; font-weight: 500; }
  .footer-info p b { font-weight: 700; }
  .footer-info .broker { font-weight: 700; font-size: 25px; }
  .brand {
    position: absolute; right: 36px; top: 1135px;
    display: flex; align-items: center; gap: 10px;
    font-weight: 700; font-size: 19px; color: var(--paper); letter-spacing: 0.3px;
  }
  .brand .mark { width: 16px; height: 16px; background: var(--teal); }
</style>
</head>
<body>
<main class="poster">
  <svg class="backdrop" width="1200" height="1200" viewBox="0 0 1200 1200">
    <defs>
      <linearGradient id="photoTone" x1="0" y1="0" x2="1" y2="1">
        <stop offset="0" stop-color="var(--teal-light)"/>
        <stop offset="0.55" stop-color="var(--teal)"/>
        <stop offset="1" stop-color="#1c2b30"/>
      </linearGradient>
    </defs>
    <path role="img" aria-label="Portrait of the managing broker in a hat and dark coat, in front of teal-toned houses"
          d="M829,0 C700,150 640,380 668,560 C690,760 760,900 850,1010 L1200,1010 L1200,0 Z"
          fill="url(#photoTone)"/>
    <path class="footer-band" d="M0,918 C250,990 520,1000 760,950 C950,910 1100,870 1200,834 L1200,1200 L0,1200 Z" fill="var(--ink)"/>
  </svg>

  <header class="headline">
    <div class="lead">WHY BE A REGULAR AGENT</div>
    <div class="lead-2">WHEN YOU CAN</div>
    <div class="big be-a">BE A</div>
    <div class="big boss">BOSS?</div>
  </header>

  <h2 class="offer">We offer four levels of<br>participation you increase<br>your earning potential at each level</h2>

  <ul class="levels">
    <li><svg class="tick" viewBox="0 0 14 14"><rect x="1" y="1" width="12" height="12" rx="3" fill="none" stroke="var(--teal)" stroke-width="1.8"/><path d="M4 7l2.2 2.2L11 3.5" fill="none" stroke="var(--teal)" stroke-width="2"/></svg><strong>Level One</strong> - Learn to Earn Additional Income Through....</li>
    <li class="detail">Mortgage Originations - Dual Licensing / No Additional Work</li>
    <li class="detail">Real Estate Investing - Invest Jointly with Us</li>
    <li class="detail">Agent Recruitment - Up to 10% Override</li>
    <li><svg class="tick" viewBox="0 0 14 14"><rect x="1" y="1" width="12" height="12" rx="3" fill="none" stroke="var(--teal)" stroke-width="1.8"/><path d="M4 7l2.2 2.2L11 3.5" fill="none" stroke="var(--teal)" stroke-width="2"/></svg><strong>Level Two</strong> - Team Leader</li>
    <li><svg class="tick" viewBox="0 0 14 14"><rect x="1" y="1" width="12" height="12" rx="3" fill="none" stroke="var(--teal)" stroke-width="1.8"/><path d="M4 7l2.2 2.2L11 3.5" fill="none" stroke="var(--teal)" stroke-width="2"/></svg><strong>Level Three</strong> - Minority Halo Franchise Ownership</li>
    <li><svg class="tick" viewBox="0 0 14 14"><rect x="1" y="1" width="12" height="12" rx="3" fill="none" stroke="var(--teal)" stroke-width="1.8"/><path d="M4 7l2.2 2.2L11 3.5" fill="none" stroke="var(--teal)" stroke-width="2"/></svg><strong>Level Four</strong> - Majority Halo Franchise Ownership</li>
  </ul>

  <footer class="footer-info">
    <h2>FOR MORE INFORMATION</h2>
    <div class="rule"></div>
    <p>visit us at <b>www.jobsathalopview.com</b></p>
    <p>and request a meeting with our</p>
    <div class="rule short"></div>
    <p class="broker">Managing Broker, Mr. Gordon Malvery.</p>
  </footer>

  <div class="brand"><span class="mark"></span>HALO PRIMEVIEW HOMES GROUP</div>
</main>
</body>
</html>
```